PACKAGING DESIGN FOR ESSENTIAL OIL

The product is argan oil and I would be selling it in 30ml amber glass bottle.
I am looking for a design to put on the bottle. The brand name is BRUME DOUCE (Soft Mist translated in english). I would be using screen printing for the design on the glass bottle.
The bottle would be put in a carton box and I would need a design for that as well. I would like the carton box to be in gold colour (but you can propose a design with any other colour for the carton as well).
I am sending a picture with measurements of the glass bottle with its cap on it.
I am also sending the details I want to be included on the carton box.
I would like a design related to Morocco as the argan oil is from Morocco.
I have uploaded images that can inspire you all for my design.
I am sending you as well a link from findpix for Moroccan Mosaic:
https://www.findpix-example.test/search?q=argan+oil+brand&source=lnms&tbm=isch&sa=X&ei=aVZaUuKfFM7nrAeS7oGQAQ&ved=0CAcQ_AUoAQ&biw=1280&bih=658&dpr=1#q=moroccan+mosaic&tbm=isch&imgdii=_
Industry/Entity Type
Screen Printing
Requirements
Must have
- The Moroccan touch must be present in the design.
I would also like to have the brand name Brume Douce hot foil printed.
Nice to have
- A design of the argan tree would be nice as it shows exactly what we are selling.

```html
<!DOCTYPE html>
<html lang="en">
<head>
<meta charset="UTF-8">
<title>Brume Douce – Argan Oil Label</title>
<link href="https://fonts.googleapis.com/css2?family=Roboto:wght@700;900&family=Audiowide&display=swap" rel="stylesheet">
<style>
  :root {
    --page: #ffffff;
    --mosaic-dark: #3a3a33;
    --mosaic-mid: #5b5a3e;
    --mosaic-gold: #8f8a3a;
    --olive-deep: #1f2412;
    --olive: #4c5a22;
    --olive-light: #7d8a3a;
    --band: rgba(92, 118, 28, 0.78);
    --gold: #ffe000;
    --white: #ffffff;
    --ink: #1a1a10;
    --leaf: #5fcf2e;
    --tag: #1e1c14;
  }
  html, body {
    margin: 0;
    padding: 0;
    width: 953px;
    height: 1200px;
    overflow: hidden;
    background: var(--page);
  }
  .label {
    position: relative;
    width: 953px;
    height: 1200px;
  }
  .mosaic {
    position: absolute;
    left: 4px;
    right: 4px;
    background:
      radial-gradient(circle at 30% 40%, rgba(240,220,40,0.18), transparent 60%),
      linear-gradient(135deg, var(--mosaic-dark), var(--mosaic-mid) 50%, var(--mosaic-dark));
  }
  .mosaic--top { top: 4px; height: 509px; border-radius: 12px 12px 0 0; }
  .mosaic--bottom { top: 732px; height: 464px; border-radius: 0 0 12px 12px; }
  .emblem {
    position: absolute;
    left: 0;
    top: 0;
    width: 953px;
    height: 1200px;
  }
  .emblem-text {
    position: absolute;
    left: 229px;
    width: 507px;
    top: 495px;
    height: 295px;
    text-align: center;
    font-family: "Roboto", Arial, sans-serif;
  }
  .brand-name {
    margin: 28px 0 0;
    font-weight: 900;
    font-size: 62px;
    line-height: 1;
    letter-spacing: 1px;
    color: var(--gold);
  }
  .product-name {
    margin: 12px 0 0;
    font-weight: 700;
    font-size: 60px;
    line-height: 1;
    letter-spacing: 1px;
    color: var(--white);
  }
  .badge-organic {
    display: block;
    width: 362px;
    height: 43px;
    margin: 20px auto 0;
    border-radius: 8px;
    background: var(--gold);
    color: var(--ink);
    font-weight: 900;
    font-size: 29px;
    line-height: 43px;
    letter-spacing: 1px;
  }
  .claim {
    margin: 6px 0 0;
    font-family: "Audiowide", "Roboto", sans-serif;
    font-size: 38px;
    line-height: 1.1;
    color: var(--leaf);
  }
  .volume {
    position: absolute;
    left: 790px;
    top: 1140px;
    width: 129px;
    height: 36px;
    background: var(--tag);
    color: var(--white);
    font-family: "Roboto", Arial, sans-serif;
    font-weight: 700;
    font-size: 24px;
    line-height: 36px;
    text-align: center;
    letter-spacing: 2px;
  }
</style>
</head>
<body>
<div class="label">
  <div class="mosaic mosaic--top" role="img" aria-label="Moroccan zellige mosaic pattern in charcoal, yellow and green"></div>
  <div class="mosaic mosaic--bottom" role="img" aria-label="Moroccan zellige mosaic pattern in charcoal, yellow and green"></div>

  <svg class="emblem" viewBox="0 0 953 1200" xmlns="http://www.w3.org/2000/svg">
    <defs>
      <linearGradient id="argan-fill" x1="0" y1="0" x2="0" y2="1">
        <stop offset="0" stop-color="#2a3014"/>
        <stop offset="0.4" stop-color="#4c5a22"/>
        <stop offset="0.7" stop-color="#3a4418"/>
        <stop offset="1" stop-color="#1c200f"/>
      </linearGradient>
      <clipPath id="arch-clip">
        <path d="M479 263 C505 300 560 330 640 380 C720 430 736 490 736 560 L736 690 C736 760 710 800 660 840 C600 890 520 940 479 999 C438 940 358 890 298 840 C248 800 229 760 229 690 L229 560 C229 490 245 430 318 380 C398 330 453 300 479 263 Z"/>
      </clipPath>
    </defs>
    <path role="img" aria-label="Photograph of argan tree branches with fruit" fill="url(#argan-fill)"
      d="M479 263 C505 300 560 330 640 380 C720 430 736 490 736 560 L736 690 C736 760 710 800 660 840 C600 890 520 940 479 999 C438 940 358 890 298 840 C248 800 229 760 229 690 L229 560 C229 490 245 430 318 380 C398 330 453 300 479 263 Z"/>
    <rect x="200" y="495" width="560" height="295" fill="var(--band)" clip-path="url(#arch-clip)"/>
  </svg>

  <div class="emblem-text">
    <h1 class="brand-name">BRUME DOUCE</h1>
    <p class="product-name">ARGAN OIL</p>
    <span class="badge-organic">ORGANIC</span>
    <p class="claim">100% NATURAL</p>
  </div>

  <div class="volume">30 ML</div>
</div>
</body>
</html>
```